Velmar Ops Business Cards

We need to design some upbeat business cards. We are an Industrial Rope Access Company/Height Safety Company that specialize in Rope Access, Confined Space, Anchor Points, Safety Systems, PPE Inspecions and Rigging.
Company name is Velmar Ops Ltd
Card is for Gareth Lomas the Company Director
His mobile number is 027 418 9072 and email is gareth@velmarops.co.nz. Website address is www.velmarops.co.nz.
We will post some pictures below to ensure you get a good idea of what we do.

```html
<!DOCTYPE html>
<html lang="en">
<head>
<meta charset="utf-8">
<title>Velmar Ops Ltd — Business Cards</title>
<link rel="stylesheet" href="https://fonts.googleapis.com/css2?family=Exo+2:ital,wght@0,600;0,700;1,600&family=Open+Sans:wght@400&display=swap">
<style>
  :root {
    --page: #e9e6e1;
    --card-black: #050608;
    --brand-blue: #1f4fd6;
    --line-blue: #1e3fd0;
    --line-cyan: #1aa0ff;
    --sky-top: #2f6fd0;
    --sky-low: #8fb9ea;
    --shadow: rgba(0, 0, 0, 0.28);
  }
  * { box-sizing: border-box; margin: 0; padding: 0; }
  html, body {
    width: 1200px;
    height: 800px;
    overflow: hidden;
    background: var(--page);
  }
  .sheet {
    position: relative;
    width: 1200px;
    height: 800px;
    display: flex;
    align-items: center;
    justify-content: center;
    gap: 50px;
  }
  .card {
    position: relative;
    width: 540px;
    height: 330px;
    background: var(--card-black);
    overflow: hidden;
    box-shadow: 0 14px 30px var(--shadow);
  }

  /* Back of card: services */
  .card-back .site-photo {
    position: absolute;
    left: 0; top: 0;
    width: 100%;
    height: 42%;
    background: linear-gradient(170deg, var(--sky-top) 0%, #4a86dc 55%, var(--sky-low) 100%);
  }
  .card-back .services {
    position: absolute;
    left: 0; top: 42%;
    width: 100%;
    height: 58%;
    padding: 14px 40px 0 52px;
    display: flex;
    gap: 34px;
    font-family: "Exo 2", sans-serif;
    font-style: italic;
    font-weight: 600;
    font-size: 19px;
    line-height: 1.18;
    color: var(--brand-blue);
  }
  .services ul { list-style: none; }
  .services li::before { content: "· "; }
  .services .col-left { padding-top: 32px; }
  .services .col-right { margin-top: -14px; }

  /* Front of card: contact */
  .card-front .work-photo {
    position: absolute;
    inset: 0;
    background:
      radial-gradient(ellipse 30% 40% at 62% 45%, rgba(220, 215, 190, 0.5), transparent 70%),
      radial-gradient(ellipse 40% 60% at 30% 15%, rgba(150, 150, 140, 0.35), transparent 70%),
      linear-gradient(160deg, #2a2a26 0%, #121210 45%, #050506 100%);
  }
  .card-front .lower-shade {
    position: absolute;
    inset: 0;
    background: linear-gradient(180deg, transparent 45%, rgba(0,0,0,0.75) 65%, rgba(0,0,0,0.9) 100%);
  }
  .card-front .swoosh {
    position: absolute;
    inset: 0;
    width: 100%;
    height: 100%;
  }
  .brand {
    position: absolute;
    left: 40px;
    top: 180px;
    font-family: "Exo 2", sans-serif;
    font-weight: 700;
    font-size: 42px;
    line-height: 1;
    letter-spacing: 1px;
    color: var(--brand-blue);
  }
  .website {
    position: absolute;
    left: 42px;
    top: 232px;
    font-family: "Exo 2", sans-serif;
    font-style: italic;
    font-weight: 600;
    font-size: 15px;
    letter-spacing: 0.5px;
    color: var(--brand-blue);
  }
  .contact {
    position: absolute;
    right: 40px;
    top: 236px;
    font-family: "Open Sans", sans-serif;
    font-weight: 400;
    font-size: 15px;
    line-height: 1.45;
    color: var(--brand-blue);
    font-style: normal;
  }
</style>
</head>
<body>
  <main class="sheet">
    <section class="card card-back" aria-label="Card back: services">
      <div class="site-photo" role="img" aria-label="Photo of rope access technicians working on a cable-stayed mast against a blue sky"></div>
      <div class="services">
        <ul class="col-left">
          <li>Rope Access</li>
          <li>Anchor Points</li>
          <li>PPE Certification</li>
          <li>Rope Access</li>
          <li>Anchor Points</li>
          <li>PPE Certification</li>
        </ul>
        <ul class="col-right">
          <li>Confined Space</li>
          <li>Safety Systems</li>
          <li>Rigging</li>
          <li>Confined Space</li>
          <li>Safety Systems</li>
          <li>Rigging</li>
        </ul>
      </div>
    </section>

    <section class="card card-front" aria-label="Card front: contact details">
      <div class="work-photo" role="img" aria-label="Photo of a technician with a head torch working inside a steel confined space"></div>
      <div class="lower-shade"></div>
      <svg class="swoosh" viewBox="0 0 540 330" preserveAspectRatio="none" aria-hidden="true">
        <defs>
          <linearGradient id="swooshBlue" x1="0" y1="0" x2="1" y2="0">
            <stop offset="0" stop-color="#1aa0ff"/>
            <stop offset="1" stop-color="#1e3fd0"/>
          </linearGradient>
        </defs>
        <path d="M0 78 Q 270 168 540 186 L 540 198 Q 270 176 0 81 Z" fill="url(#swooshBlue)"/>
      </svg>
      <div class="brand">Velmar Ops</div>
      <div class="website">www.velmarops.co.nz</div>
      <address class="contact">
        Gareth Lomas - Director<br>
        027 418 9072<br>
        gareth@velmarops.co.nz
      </address>
    </section>
  </main>
</body>
</html>
```